Storage Auctions Book Cover

I need a new cover for my book which is located here:
http://www.quillmart-example.com/dp/R417TZ2WQX/
The book is about making money by buying storage units at auction, made popular by the reality shows "Locker Clash" and "Gavel Trackers." It's for entrepreneurs and those looking for a weekend business.
The current cover was homemade in Gimp, and it's holding back sales. I think it needs a better cover in order to look more professional and catch more attention.
Updates
So far, I really like the designs from Pimbleworth and vostacraft. Consider those two what I'm looking for, they are both good.
Industry/Entity Type
Storage
Look and feel
Each slider illustrates characteristics of the customer's brand and the style your logo design should communicate.

```html
<!DOCTYPE html>
<html lang="en">
<head>
<meta charset="utf-8">
<title>Making Money in Storage Auctions – Book Cover</title>
<link rel="stylesheet" href="https://fonts.googleapis.com/css2?family=Anton&family=Roboto+Condensed:ital,wght@1,700&display=swap">
<style>
  :root {
    --wall-dark: #2b2823;
    --wall-mid: #4d463d;
    --door-green: #2e5a36;
    --door-green-light: #4e7c4f;
    --ground: #55524e;
    --ground-dark: #2f2e2c;
    --title-yellow: #f2c316;
    --title-edge: #1c1a12;
    --banner-fill: #f6f1e4;
    --banner-red: #c8201c;
    --subtitle-white: #ffffff;
    --box-tan: #d3a774;
    --box-dark: #a97b4b;
    --author-red: #b3241d;
    --money-light: #c9d6bd;
    --money-green: #8aa27a;
    --money-dark: #55704a;
  }
  * { margin: 0; padding: 0; box-sizing: border-box; }
  html, body { width: 807px; height: 1200px; overflow: hidden; background: #fff; }
  .cover {
    position: relative;
    width: 807px;
    height: 1200px;
    overflow: hidden;
  }
  .scene-backdrop {
    position: absolute;
    inset: 0;
    background: linear-gradient(to bottom, var(--wall-mid) 0%, var(--wall-dark) 60%, var(--ground) 75%, var(--ground-dark) 100%);
  }
  .storage-door {
    position: absolute;
    left: 40px; top: 170px;
    width: 727px; height: 700px;
    background: radial-gradient(ellipse at 50% 40%, var(--door-green-light), var(--door-green) 80%);
  }
  .title {
    position: absolute;
    left: 0; right: 0;
    text-align: center;
    font-family: 'Anton', Impact, sans-serif;
    font-weight: 400;
    color: var(--title-yellow);
    text-transform: uppercase;
    line-height: 1;
    font-size: 238px;
    letter-spacing: 2px;
    -webkit-text-stroke: 3px var(--title-edge);
    text-shadow: 5px 7px 0 var(--title-edge);
  }
  .title-making { top: 210px; }
  .title-money { top: 400px; }
  .subtitle-banner {
    position: absolute;
    left: 96px; top: 640px;
    width: 622px; height: 96px;
    background: var(--banner-fill);
    box-shadow: 3px 4px 6px rgba(0,0,0,0.5);
    display: flex; align-items: center; justify-content: center;
    font-family: 'Anton', Impact, sans-serif;
    font-size: 58px;
    color: var(--banner-red);
    text-transform: uppercase;
    letter-spacing: 1px;
  }
  .subtitle {
    position: absolute;
    left: 60px; right: 60px; top: 752px;
    text-align: center;
    font-family: 'Roboto Condensed', 'Arial Narrow', sans-serif;
    font-weight: 700;
    font-style: italic;
    font-size: 32px;
    line-height: 1.2;
    color: var(--subtitle-white);
    text-shadow: 2px 2px 3px rgba(0,0,0,0.8);
  }
  .cardboard-box {
    position: absolute;
    left: 40px; top: 870px;
    width: 245px; height: 235px;
    background: linear-gradient(135deg, var(--box-tan), var(--box-dark));
  }
  .author {
    position: absolute;
    left: 110px; top: 910px;
    width: 170px;
    text-align: center;
    font-family: 'Anton', Impact, sans-serif;
    font-size: 30px;
    line-height: 1.2;
    color: var(--author-red);
    text-transform: uppercase;
  }
  .author .by { font-size: 20px; }
  .money-pile {
    position: absolute;
    left: 285px; top: 860px;
    width: 510px; height: 320px;
    border-radius: 35% 35% 20% 20%;
    background: radial-gradient(ellipse at 50% 45%, var(--money-light), var(--money-green) 65%, var(--money-dark));
  }
</style>
</head>
<body>
  <div class="cover">
    <div class="scene-backdrop" role="img" aria-label="Dark storage facility wall and concrete ground"></div>
    <div class="storage-door" role="img" aria-label="Green roll-up storage unit door"></div>
    <h1 class="title title-making">Making</h1>
    <h1 class="title title-money">Money</h1>
    <div class="subtitle-banner">In Storage Auctions</div>
    <p class="subtitle">How to Profit from the Locker Clash and<br>become a Storage Auction Warrior</p>
    <div class="money-pile" role="img" aria-label="Scattered stacks of banded hundred-dollar bills"></div>
    <div class="cardboard-box" role="img" aria-label="Closed cardboard moving box"></div>
    <p class="author"><span class="by">By</span> Dalton<br>Meyers</p>
  </div>
</body>
</html>
```